Create a 2-sided postcard design (standard size) for Torvane Systems, a professional low-voltage and security integration company.
Side 1 – Front (Marketing Side)
Headline / Intro:
"Torvane Systems – Security, Connectivity, and Peace of Mind."
Brief Overview / Summary:
Torvane Systems provides complete security and technology integration solutions for commercial, industrial, and multifamily properties. From access control to fire systems, we specialize in delivering seamless, scalable, and reliable installations supported by professional service and ongoing care.
Services Breakdown:
Access Control – Cloud-based and enterprise access solutions to manage entry and permissions.
CCTV / Video Surveillance – Protect your property with high-definition cameras and remote monitoring.
Intrusion Alarm – Professional-grade systems to detect and deter unauthorized access.
Audio-Visual – From conference rooms to distributed audio and digital displays.
Fire Systems – Code-compliant alarm systems with 24/7 UL monitoring and life-safety support.
Structured Data Cabling – Low-voltage and fiber cabling for reliable network infrastructure.
Trusted By (Logos):
Melo, Plivantex, Grovelink, Carrow Investments, Bluff Hardware, Pinefold Games, Ledgerline Property Consultants, TRUEform
Technology partners:
Include logos of brands like Quelt, Otter Bank Networks, RMT , Lumen Sentrywell, Solmira, JFT, Blazecor
Contact Info:
📧 sales@torvanesystems.example
📞 760-555-0142
🌐 torvanesystems.example
🖼️ Side 2 – Back (Branding Side)
Primary Focus:
Large, centered Torvane Systems logo.
Subtext / Tagline (Optional):
“Your Security and Technology Partner.”
List of Services (Under Logo):
Access Control | CCTV | Intrusion Alarm | Audio-Visual | Fire | Data
🎨 Design Preferences:
Clean, modern, and professional layout.
Corporate tones (e.g., black and white, bold accents).
Use clean typography and icons for service areas.
Logo should be prominent on the back and represent the brand with strength and clarity.
Open to designer layout and creative interpretation as long as it stays on brand.

```html
<!DOCTYPE html>
<html lang="en">
<head>
<meta charset="utf-8">
<title>Torvane Systems – Postcard</title>
<link href="https://fonts.googleapis.com/css2?family=Poppins:wght@400;500;600;700&display=swap" rel="stylesheet">
<style>
  :root{
    --page:#e9e9ea;
    --card:#0d1317;
    --panel:#080c0f;
    --blue:#1f76c6;
    --teal:#5cc7d7;
    --white:#ffffff;
    --muted:#d9dee2;
  }
  *{box-sizing:border-box;margin:0;padding:0}
  html,body{width:1200px;height:2299px;overflow:hidden}
  body{background:var(--page);font-family:'Poppins',sans-serif;color:var(--white);position:relative}
  .card{position:absolute;left:50px;width:1100px;height:734px;background:var(--card);overflow:hidden;box-shadow:0 10px 30px rgba(0,0,0,.18)}
  .card--branding{top:385px}
  .card--marketing{top:1160px}

  /* Branding side */
  .band{position:absolute;left:706px;top:0;width:323px;height:100%;
    background:linear-gradient(180deg,#2479c8 0%,#123554 28%,#0d1317 48%,#153f66 75%,#1f74c4 100%)}
  .band__square{position:absolute;left:86px;top:292px;width:150px;height:150px;border:14px solid var(--white)}
  .lockup{position:absolute;left:69px;top:112px;display:flex;align-items:center;gap:26px}
  .lockup__square{width:120px;height:120px;border:12px solid var(--white);flex:none}
  .lockup__name{line-height:1}
  .lockup__main{display:block;font-weight:700;font-size:92px;letter-spacing:-2px}
  .lockup__sub{display:block;font-weight:600;font-size:50px;letter-spacing:17px;margin-top:6px}
  .tagline{position:absolute;left:70px;top:308px;font-weight:600;font-size:29px}
  .service-pill{position:absolute;left:63px;top:379px;width:584px;height:35px;border-radius:18px;background:var(--blue);
    font-weight:600;font-size:16px;display:flex;align-items:center;justify-content:center;white-space:nowrap}
  .phone{position:absolute;left:64px;top:455px;font-weight:700;font-size:62px;color:var(--teal);letter-spacing:-1px}
  .contact{position:absolute;left:68px;top:545px;font-weight:600;font-size:31px;line-height:38px}

  /* Marketing side */
  .mini-lockup{position:absolute;left:57px;top:58px;display:flex;align-items:center;gap:14px}
  .mini-lockup__square{width:56px;height:56px;border:6px solid var(--white)}
  .mini-lockup__main{display:block;font-weight:700;font-size:40px;line-height:1;letter-spacing:-1px}
  .mini-lockup__sub{display:block;font-weight:600;font-size:22px;line-height:1;letter-spacing:7px;margin-top:2px}
  .overview{position:absolute;left:57px;top:150px;width:442px;font-size:14px;line-height:15.5px;text-align:justify;color:var(--muted)}
  .services{position:absolute;left:41px;top:250px;width:458px;height:500px;background:var(--panel);border-radius:24px 24px 0 0;padding:26px 22px 0 20px}
  .service{display:flex;gap:16px;height:72px}
  .service__icon{width:48px;height:48px;flex:none;margin-top:4px}
  .service__title{font-weight:600;font-size:18px;line-height:22px}
  .service__text{font-size:13px;line-height:15px;color:var(--muted);text-align:justify}
  .headline{position:absolute;left:547px;top:36px;width:520px;text-align:center;font-weight:700;font-size:54px;line-height:1;color:var(--teal);letter-spacing:-1px;white-space:nowrap}
  .subhead{position:absolute;left:538px;top:108px;width:540px;text-align:center;font-weight:600;font-size:23px;white-space:nowrap}
  .hero{position:absolute;left:538px;top:154px;width:562px;height:335px;border-radius:22px 0 0 22px;
    background:radial-gradient(circle at 38% 45%,#2f8fe0 0%,#1a4d86 22%,#12233a 55%,#0e1620 100%)}
  .trusted{position:absolute;left:537px;top:546px;width:497px;height:152px;border:3px solid var(--white);border-radius:18px}
  .trusted__pill{position:absolute;left:50%;top:-20px;transform:translateX(-50%);background:var(--teal);border-radius:20px;padding:2px 22px;font-weight:600;font-size:27px;line-height:34px;white-space:nowrap}
  .trusted__row{position:absolute;left:18px;right:18px;display:flex;justify-content:space-between;align-items:center}
  .trusted__row--one{top:42px}
  .trusted__row--two{top:96px}
  .partner{font-weight:600;font-size:15px;white-space:nowrap}
  .partner--lg{font-size:22px}
</style>
</head>
<body>

<section class="card card--branding">
  <div class="lockup">
    <div class="lockup__square"></div>
    <div class="lockup__name">
      <span class="lockup__main">TORVANE</span>
      <span class="lockup__sub">SYSTEMS</span>
    </div>
  </div>
  <p class="tagline">Your Security and Technology Partner.</p>
  <div class="service-pill">Access Control&nbsp; | &nbsp;CCTV&nbsp; | &nbsp;Intrusion Alarm&nbsp; | &nbsp;Audio-Visual&nbsp; | &nbsp;Fire&nbsp; | &nbsp;Data</div>
  <p class="phone">760-555-0142</p>
  <p class="contact">sales@torvanesystems.example<br>torvanesystems.example</p>
  <div class="band"><div class="band__square"></div></div>
</section>

<section class="card card--marketing">
  <div class="mini-lockup">
    <div class="mini-lockup__square"></div>
    <div>
      <span class="mini-lockup__main">TORVANE</span>
      <span class="mini-lockup__sub">SYSTEMS</span>
    </div>
  </div>
  <p class="overview">Torvane Systems provides complete security and technology integration solutions for commercial, industrial, and multifamily properties. From access control to fire systems, we specialize in delivering seamless, scalable, and reliable installations supported by professional service and ongoing care.</p>

  <div class="services">
    <div class="service">
      <svg class="service__icon" viewBox="0 0 48 48" fill="none" stroke="#5cc7d7" stroke-width="2"><path d="M15 22v-8a9 9 0 0 1 18 0v8"/><rect x="11" y="22" width="26" height="22" rx="2"/><path d="M24 31v5"/></svg>
      <div><p class="service__title">Access Control</p><p class="service__text">Cloud-based and enterprise access solutions to manage entry and permissions.</p></div>
    </div>
    <div class="service">
      <svg class="service__icon" viewBox="0 0 48 48" fill="none" stroke="#5cc7d7" stroke-width="2"><circle cx="24" cy="24" r="20"/><circle cx="24" cy="24" r="11"/></svg>
      <div><p class="service__title">CCTV / Video Surveillance</p><p class="service__text">Protect your property with high-definition cameras and remote monitoring.</p></div>
    </div>
    <div class="service">
      <svg class="service__icon" viewBox="0 0 48 48" fill="none" stroke="#5cc7d7" stroke-width="2"><circle cx="8" cy="8" r="5"/><circle cx="24" cy="8" r="5"/><circle cx="40" cy="8" r="5"/><circle cx="8" cy="24" r="5"/><circle cx="24" cy="24" r="5"/><circle cx="40" cy="24" r="5"/><circle cx="8" cy="40" r="5"/><circle cx="24" cy="40" r="5"/><circle cx="40" cy="40" r="5"/></svg>
      <div><p class="service__title">Intrusion Alarm</p><p class="service__text">Professional-grade systems to detect and deter unauthorized access.</p></div>
    </div>
    <div class="service">
      <svg class="service__icon" viewBox="0 0 48 48" fill="none" stroke="#5cc7d7" stroke-width="2"><rect x="3" y="6" width="42" height="28" rx="2"/><path d="M24 34v8M14 44h20M10 12v14h8"/></svg>
      <div><p class="service__title">Audio-Visual</p><p class="service__text">From conference rooms to distributed audio and digital displays.</p></div>
    </div>
    <div class="service">
      <svg class="service__icon" viewBox="0 0 48 48" fill="none" stroke="#5cc7d7" stroke-width="2"><path d="M24 4c3 9 13 15 13 27a13 13 0 0 1-26 0c0-7 4-11 6-14 1 5 3 7 5 8 0-8 2-15 2-21z"/></svg>
      <div><p class="service__title">Fire Systems</p><p class="service__text">Code-compliant alarm systems with 24/7 UL monitoring and life-safety support.</p></div>
    </div>
    <div class="service">
      <svg class="service__icon" viewBox="0 0 48 48" fill="none" stroke="#5cc7d7" stroke-width="2"><rect x="14" y="4" width="30" height="40" rx="2"/><path d="M20 12h18M20 20h18M20 28h18M20 36h18M4 16h10M4 26h10M4 36h10"/></svg>
      <div><p class="service__title">Structured Data Cabling</p><p class="service__text">Low-voltage and fiber cabling for reliable network infrastructure.</p></div>
    </div>
  </div>

  <h1 class="headline">TORVANE SYSTEMS</h1>
  <p class="subhead">Security, Connectivity, and Peace of Mind.</p>
  <div class="hero" role="img" aria-label="Photo of an open hand holding a glowing blue security shield with a padlock"></div>

  <div class="trusted">
    <span class="trusted__pill">Trusted By</span>
    <div class="trusted__row trusted__row--one">
      <span class="partner">Ledgerline</span>
      <span class="partner partner--lg">Quelt</span>
      <span class="partner">Pinefold Games</span>
      <span class="partner partner--lg">TRUEform</span>
    </div>
    <div class="trusted__row trusted__row--two">
      <span class="partner">Solmira</span>
      <span class="partner">Melo</span>
      <span class="partner partner--lg">JFT</span>
      <span class="partner">Blazecor</span>
      <span class="partner">Lumen Sentrywell</span>
    </div>
  </div>
</section>

</body>
</html>
```